shopfitters cards and stationery
Stationery
Project: shopfitters cards and stationery
shopfitters cards and stationery  - Construction
Creative Brief
Professional
Mark Pelling
Contracts Manager
7/24 Quarry Lane Wendale 4182
mark@fitwrightgroup.com.au
www.fitwrightgroup.com.au
Phone numbers and other details etc will change if you could use them for know that will be great. give me your best work :) Thanks

```html
<!DOCTYPE html>
<html lang="en">
<head>
<meta charset="utf-8">
<title>Fitwright Group Stationery</title>
<link rel="stylesheet" href="https://fonts.googleapis.com/css2?family=Michroma&display=swap">
<style>
  :root {
    --bg: #e8eaed;
    --paper: #ffffff;
    --blue: #1c3a9e;
    --blue-deep: #10237a;
    --grey-dark: #4a4b50;
    --grey-light: #a9abb1;
    --ink: #4b4d55;
  }
  * { margin: 0; padding: 0; box-sizing: border-box; }
  html, body { width: 1200px; height: 936px; overflow: hidden; }
  body { background: var(--bg); font-family: "Michroma", sans-serif; color: var(--ink); position: relative; }

  .sheet { position: absolute; background: var(--paper); box-shadow: 0 2px 6px rgba(0,0,0,.12); overflow: hidden; }

  /* decorative corner area, shown as a soft tonal fill */
  .corner-accent {
    position: absolute; right: 0; bottom: 0;
    background: radial-gradient(ellipse at 100% 100%, rgba(28,58,158,.28) 0%, rgba(74,75,80,.16) 45%, rgba(169,171,177,0) 75%);
  }

  .brand { display: flex; align-items: center; gap: 8px; }
  .brand-dot { border-radius: 50%; background: var(--blue); flex: none; }
  .brand-name { font-family: "Michroma", sans-serif; color: var(--blue); line-height: 1.05; letter-spacing: .04em; white-space: nowrap; }

  /* letterhead */
  .letterhead { left: 183px; top: 66px; width: 390px; height: 548px; }
  .letterhead .brand { position: absolute; left: 24px; top: 26px; }
  .letterhead .brand-dot { width: 24px; height: 24px; }
  .letterhead .brand-name { font-size: 12px; }
  .contact-list { position: absolute; left: 238px; top: 26px; list-style: none; font-size: 5.5px; line-height: 9px; letter-spacing: .06em; white-space: nowrap; }
  .contact-list li::before { content: ""; display: inline-block; width: 4px; height: 4px; border-radius: 50%; background: var(--blue); margin-right: 4px; vertical-align: middle; }

  /* folder */
  .folder { left: 637px; top: 38px; width: 461px; height: 578px; }
  .folder .brand { position: absolute; left: 0; right: 0; top: 230px; flex-direction: column; gap: 12px; }
  .folder .brand-dot { width: 64px; height: 64px; }
  .folder .brand-name { font-size: 26px; text-align: center; }

  /* business cards */
  .card-front { left: 38px; top: 655px; width: 198px; height: 76px; }
  .card-front .brand { position: absolute; left: 12px; top: 14px; gap: 5px; }
  .card-front .brand-dot { width: 14px; height: 14px; }
  .card-front .brand-name { font-size: 7px; }
  .card-back { left: 38px; top: 774px; width: 198px; height: 101px; background: linear-gradient(135deg, var(--blue) 0%, var(--blue-deep) 100%); }
  .card-back .web { position: absolute; left: 12px; bottom: 12px; font-size: 5px; color: #9fb0e6; letter-spacing: .12em; }

  /* envelopes */
  .env-front { left: 266px; top: 672px; width: 432px; height: 203px; }
  .env-front .brand { position: absolute; left: 20px; top: 20px; gap: 6px; }
  .env-front .brand-dot { width: 20px; height: 20px; }
  .env-front .brand-name { font-size: 10px; }
  .env-front .address { position: absolute; left: 48px; top: 50px; font-size: 5.5px; letter-spacing: .1em; white-space: nowrap; }
  .env-back { left: 738px; top: 672px; width: 378px; height: 203px; }
  .env-flap { position: absolute; left: 0; top: 0; }
  .env-back .web { position: absolute; left: 0; right: 0; top: 18px; text-align: center; font-size: 6.5px; color: #e3e8fb; letter-spacing: .3em; white-space: nowrap; }
</style>
</head>
<body>

<section class="sheet letterhead" aria-label="Letterhead">
  <div class="brand"><span class="brand-dot"></span><span class="brand-name">FITWRIGHT<br>GROUP</span></div>
  <ul class="contact-list">
    <li>7/24 Quarry Lane Wendale 4182</li>
    <li>P 07 3390 4410</li>
    <li>F 07 3390 4411</li>
    <li>M 0412 558 190</li>
    <li>mark@fitwrightgroup.com.au</li>
    <li>www.fitwrightgroup.com.au</li>
  </ul>
  <div class="corner-accent" role="img" aria-label="Corner swoosh decoration in blue and grey" style="width:190px;height:150px"></div>
</section>

<section class="sheet folder" aria-label="Presentation folder">
  <div class="brand"><span class="brand-dot"></span><span class="brand-name">FITWRIGHT<br>GROUP</span></div>
  <div class="corner-accent" role="img" aria-label="Corner swoosh decoration in blue and grey" style="width:220px;height:170px"></div>
</section>

<section class="sheet card-front" aria-label="Business card front">
  <div class="brand"><span class="brand-dot"></span><span class="brand-name">FITWRIGHT<br>GROUP</span></div>
  <div class="corner-accent" role="img" aria-label="Corner swoosh decoration in blue and grey" style="width:110px;height:60px"></div>
</section>

<section class="sheet card-back" aria-label="Business card back">
  <span class="web">www.fitwrightgroup.com.au</span>
</section>

<section class="sheet env-front" aria-label="Envelope front">
  <div class="brand"><span class="brand-dot"></span><span class="brand-name">FITWRIGHT<br>GROUP</span></div>
  <p class="address">7/24 Quarry Lane Wendale 4182</p>
  <div class="corner-accent" role="img" aria-label="Corner swoosh decoration in blue and grey" style="width:180px;height:120px"></div>
</section>

<section class="sheet env-back" aria-label="Envelope back">
  <svg class="env-flap" width="378" height="110" viewBox="0 0 378 110">
    <defs>
      <linearGradient id="flap-fill" x1="0" y1="0" x2="1" y2="1">
        <stop offset="0" stop-color="#1c3a9e"/>
        <stop offset="1" stop-color="#10237a"/>
      </linearGradient>
    </defs>
    <path d="M0,0 H378 V58 L218,104 Q189,112 160,104 L0,58 Z" fill="url(#flap-fill)"/>
  </svg>
  <span class="web">www.fitwrightgroup.com.au</span>
</section>

</body>
</html>
```